Dastrelo's New Trucking Company Website

We are wanting to create a basic website for “Dastrelo Trucking” on www.DastreloTrucking.example.

The first attachment titled “write-up” has 7 sections listed, which we would like as tabs at the top of the website, followed by the write up of that section. (The sections ‘employment’ and ‘requirements’ should be under one section).

We would like the landing page to be that of a photo of a Dastrelo Truck. Please see attachment two “Dastrelo_truck” as an example of what our truck looks like. We would like this to be of better quality/more pleasing to the eye. The rest of the attachments (attachment 3- attachment 7) are of possible photos/ideas.

Woould you be able to photoshop any of those trucks to look like our Dastrelo Truck on to a pretty highway/background etc?

We would like this main photo be a constant background of the website, even when you click around the website and the language changes.

Target Market(s)

Northwest Based Companies seeking Transportation needs, grocery stores, Truck Drivers

Industry/Entity Type

Trucking Company

Number of Pages Required

5+ page

Font styles to use
Sans Serif

Requirements
Must have
• Must have one really good photo of our truck (or a truck that looks like ours) as the main photo on the page. This photo must stay consistent as the background when people click on the tabs/sections below.
Nice to have
• Clean/simple layout
Should not have
• Dull colors/ disorganized.

```html
<!DOCTYPE html>
<html lang="en">
<head>
<meta charset="utf-8">
<title>Dastrelo Trucking</title>
<link href="https://fonts.googleapis.com/css2?family=Poppins:wght@300;400;500;600&display=swap" rel="stylesheet">
<style>
:root{
  --orange:#ec6a1a;
  --dark:#262626;
  --darker:#1f1f1f;
  --text:#555;
  --muted:#8a8a8a;
  --light:#f4f4f4;
  --line:#e6e6e6;
  --white:#fff;
}
*{box-sizing:border-box;margin:0;padding:0}
html,body{width:1200px;height:3098px;overflow:hidden}
body{font-family:'Poppins',sans-serif;color:var(--text);background:var(--white);position:relative}
.abs{position:absolute}
a{color:inherit;text-decoration:none}
ul{list-style:none}

/* top bar */
.topbar{top:0;left:0;width:1200px;height:30px;background:var(--dark);color:#9a9a9a;font-size:11px}
.topbar .follow{left:155px;top:8px;display:flex;align-items:center;gap:9px}
.topbar .dot{width:8px;height:8px;background:#8a8a8a;border-radius:2px}
.topbar .hours{right:157px;top:8px}

/* header */
.header{top:30px;left:0;width:1200px;height:150px;background:var(--white);border-bottom:1px solid var(--line)}
.brand{left:158px;top:22px;display:flex;align-items:center;gap:8px}
.brand .mark{width:30px;height:30px;border-radius:50%;background:var(--orange)}
.brand .name{font-size:14px;font-weight:600;color:var(--orange);letter-spacing:.5px}
.contact{top:26px;display:flex;align-items:center;gap:14px;font-size:11.5px;line-height:16px;color:#666}
.contact .ico{width:40px;height:40px;border:1.5px solid var(--orange);border-radius:50%;display:flex;align-items:center;justify-content:center}
.nav{left:155px;top:110px;display:flex;font-size:11.5px;color:#444}
.nav li{padding:0 14px;border-left:1px solid #ddd;line-height:12px}
.nav li:first-child{padding-left:0;border:none}
.nav li.active{color:var(--orange);position:relative}
.nav li.active::after{content:"";position:absolute;left:0;bottom:-26px;width:34px;height:2px;background:var(--orange)}
.quote-btn{right:157px;top:103px;background:var(--orange);color:var(--white);font-size:11.5px;padding:8px 15px;border-radius:2px}

/* hero */
.hero{top:180px;left:0;width:1200px;height:400px;overflow:hidden;
  background:linear-gradient(180deg,#8d9aa4 0%,#6d7a84 35%,#4b5358 60%,#3a3d3e 100%)}
.hero .truck{left:745px;top:95px;width:155px;height:290px;background:linear-gradient(180deg,#9c3a2c,#6a2a22);opacity:.85}
.hero h1{left:155px;top:132px;font-size:29px;font-weight:400;color:var(--white)}
.hero p{left:155px;top:165px;width:410px;font-size:14px;line-height:25px;color:#eee}
.hero .btn{left:155px;top:228px;border:1.5px solid var(--white);color:var(--white);font-size:11px;padding:8px 20px}
.hero .prev{left:75px;top:190px;color:var(--orange);font-size:11px;display:flex;gap:6px;align-items:center}
.hero .next{right:75px;top:190px;color:var(--white);font-size:11px;display:flex;gap:6px;align-items:center}

/* about */
.about-text{left:155px;top:640px;width:358px;text-align:right;font-size:11px;line-height:18px;color:#666}
.about-text p{margin-bottom:16px}
.about-text .sig{margin-top:62px;font-size:11px;color:#333}
.about-text .sig b{font-weight:600}
.about-head{left:535px;top:640px;line-height:22px}
.about-head .k{font-size:19px;color:#b8b8b8;font-weight:300}
.about-head .v{font-size:19px;color:var(--orange);font-weight:500}
.about-photo{left:535px;top:708px;width:205px;height:237px;background:linear-gradient(160deg,#b7c7cf,#5b6670 55%,#2b2f33)}
.exp-box{left:765px;top:708px;width:278px;height:158px;background:var(--light);padding:10px}
.exp-box .inner{background:var(--white);width:100%;height:100%;text-align:center;padding-top:30px}
.exp-box .num{font-size:46px;font-weight:300;color:#777;line-height:50px}
.exp-box .lbl{font-size:11px;color:var(--orange)}
.about-call{left:765px;top:876px;width:280px;font-size:11px;line-height:18px;color:#666}
.about-phone{left:765px;top:918px;font-size:25px;color:var(--orange);display:flex;align-items:center;gap:8px}
.ghost{left:38px;top:890px;font-size:56px;font-weight:600;color:#f3f3f3;white-space:nowrap}

/* section titles */
.sec-title{font-size:23px;color:#222;font-weight:500}
.sec-title::after{content:"";display:block;width:52px;height:2px;background:var(--orange);margin-top:12px}
.center{text-align:center;left:0;width:1200px}
.center.sec-title::after{margin-left:auto;margin-right:auto}

/* services */
.services{top:1076px;left:0;width:1200px;height:440px;display:flex}
.service{width:300px;height:440px;position:relative;display:flex;flex-direction:column;align-items:center;justify-content:center;color:var(--white)}
.service.s1{background:linear-gradient(160deg,#6d7276,#3d3f41 60%,#2b2a28)}
.service.s3{background:linear-gradient(160deg,#5b4a3f,#3a302a 60%,#2a2522)}
.service.s4{background:linear-gradient(160deg,#47544b,#2f3a33 60%,#1e2320)}
.service.active{background:var(--orange)}
.service .ico{width:56px;height:56px;border:1.5px solid rgba(255,255,255,.85);border-radius:50%;display:flex;align-items:center;justify-content:center;margin-bottom:12px}
.service h3{font-size:21px;font-weight:400;letter-spacing:.5px}
.service p{font-size:11px;line-height:18px;text-align:center;width:225px;margin-top:14px}
.service .btn{margin-top:18px;border:1.5px solid var(--white);font-size:11px;padding:6px 20px}
.pager{display:flex;gap:22px;font-size:11px;align-items:center}
.pager .prev{color:var(--orange);display:flex;gap:6px;align-items:center}
.pager .next{color:#222;display:flex;gap:6px;align-items:center}

/* testimonials */
.testimonials{top:1615px;left:0;width:1200px;height:380px;background:#f5f5f5}
.avatar{left:235px;top:140px;width:120px;height:120px;border-radius:50%;background:radial-gradient(circle at 50% 45%,#d8a58c,#7a4a32 70%)}
.quote{left:420px;top:150px;width:548px;font-size:11px;line-height:20px;color:#777}
.qmark{font-size:46px;color:#ccc;line-height:1}
.author{left:420px;top:240px;font-size:15px;color:#333;display:flex;align-items:center;gap:10px}
.author::before{content:"";width:18px;height:1px;background:#999}
.author-meta{left:420px;top:266px;font-size:10.5px;color:#888}
.arrow-btn{width:32px;height:32px;border-radius:50%;border:1.5px solid #999;display:flex;align-items:center;justify-content:center}
.dots{left:0;width:1200px;top:310px;display:flex;justify-content:center;gap:6px}
.dots span{width:7px;height:7px;border-radius:50%;border:1px solid var(--orange)}
.dots span.on{background:var(--orange)}

/* blogs */
.blog-head{left:155px;top:2055px}
.blog-pager{right:157px;top:2060px}
.blog-rule{left:155px;top:2128px;width:888px;height:1px;background:var(--line)}
.blog-feature{left:155px;top:2163px;width:433px;height:279px;background:linear-gradient(160deg,#5a3b2a,#3b2b24 45%,#1f1d1c);color:var(--white);padding:30px}
.blog-feature h4{font-size:12px;font-weight:400}
.blog-feature .date{margin-top:38px;font-size:11px;color:var(--orange);font-style:italic}
.blog-feature p{font-size:11px;line-height:18px;margin-top:70px}
.blog-feature .more{margin-top:14px;font-size:11px}
.blog-card{top:2163px;width:203px;height:279px;border:1px solid var(--line)}
.blog-card .top{background:#efefef;height:120px;padding:30px 28px}
.blog-card h4{font-size:11.5px;font-weight:400;line-height:19px;color:#444}
.blog-card .date{font-size:11px;color:var(--orange);font-style:italic;margin-top:10px;display:flex;gap:5px;align-items:center}
.blog-card .body{padding:22px 28px;font-size:11px;line-height:19px;color:#777}
.blog-card .more{margin-top:14px;color:#333}

/* map */
.map{top:2505px;left:0;width:1200px;height:200px;background:linear-gradient(135deg,#e4e4e4,#d6d6d6 50%,#e8e8e8)}

/* footer */
.footer{top:2705px;left:0;width:1200px;height:393px;background:var(--darker);color:#ccc}
.fcol{top:70px;width:220px}
.fcol h5{font-size:16px;font-weight:400;color:#eee;margin-bottom:22px;letter-spacing:.5px}
.fcol li{font-size:11px;line-height:21px;color:#bbb}
.fcol li.on{color:var(--orange)}
.fcontact li{display:flex;gap:8px;align-items:flex-start;line-height:18px;margin-bottom:4px}
.totop{left:580px;top:282px;width:40px;height:40px;border-radius:50%;background:#333;display:flex;align-items:center;justify-content:center}
.copy{left:0;width:1200px;top:352px;text-align:center;font-size:11px;color:#aaa}
</style>
</head>
<body>

<div class="abs topbar">
  <div class="abs follow">Follow Us : <span class="dot"></span><span class="dot"></span><span class="dot"></span><span class="dot"></span></div>
  <div class="abs hours">Monday - Friday : 09:00 - 18:00</div>
</div>

<header class="abs header">
  <div class="abs brand"><span class="mark"></span><span class="name">DASTRELO TRUCKING</span></div>
  <div class="abs contact" style="left:578px">
    <span class="ico"><svg width="16" height="16" viewBox="0 0 24 24" fill="none" stroke="#ec6a1a" stroke-width="2"><path d="M22 2 11 13M22 2l-7 20-4-9-9-4z"/></svg></span>
    <div>Call Us: +206-555-0147<br>dispatch@dastrelotrucking.example</div>
  </div>
  <div class="abs contact" style="left:838px">
    <span class="ico"><svg width="16" height="16" viewBox="0 0 24 24" fill="none" stroke="#ec6a1a" stroke-width="2"><path d="M12 22s7-7 7-12a7 7 0 0 0-14 0c0 5 7 12 7 12z"/><circle cx="12" cy="10" r="2.5"/></svg></span>
    <div>27/412 Harlow Rd<br>Glenmere Park VIC 3150</div>
  </div>
  <ul class="abs nav">
    <li class="active">Home</li><li>About Us</li><li>Services</li><li>Dispatch</li><li>Equipment</li><li>Safety</li><li>Insurance</li><li>Contact Us</li>
  </ul>
  <a class="abs quote-btn">Get a Free Quote</a>
</header>

<section class="abs hero" role="img" aria-label="Red container truck driving on a coastal highway beside mountains">
  <div class="abs truck"></div>
  <h1 class="abs">Our Mission</h1>
  <p class="abs">Is to provide the best customer service and trucking services in the Northwest.</p>
  <a class="abs btn">Our Services &#10140;</a>
  <div class="abs prev"><svg width="20" height="10" viewBox="0 0 20 10"><path d="M20 5H2M6 1 2 5l4 4" stroke="#ec6a1a" stroke-width="1.5" fill="none"/></svg>PREV</div>
  <div class="abs next">NEXT<svg width="20" height="10" viewBox="0 0 20 10"><path d="M0 5h18M14 1l4 4-4 4" stroke="#fff" stroke-width="1.5" fill="none"/></svg></div>
</section>

<div class="abs ghost">Dastrelo Trucking</div>
<div class="abs about-text">
  <p>Dastrelo Trucking LLC was created in 2012 to assist its parent company, Dastrelo Gourmet, in transporting product from our Seattle HQ to our Portland distribution center every night.</p>
  <p>Approximately four years later, Dastrelo Trucking has expanded to meet the growing needs of our sister company as well as many Northwest based companies looking to transport chilled, frozen and dry product.</p>
  <div class="sig"><b>Loreum Name</b> - CEO Founder</div>
</div>
<div class="abs about-head"><div class="k">ABOUT</div><div class="v">DASTRELO TRUCKING</div></div>
<div class="abs about-photo" role="img" aria-label="Black refrigerated trailer truck parked at a depot"></div>
<div class="abs exp-box"><div class="inner"><div class="num">04</div><div class="lbl">Years Experiance</div></div></div>
<div class="abs about-call">Contact our Dastrelo Trucking representative or call us at :</div>
<div class="abs about-phone"><svg width="18" height="18" viewBox="0 0 24 24" fill="#ec6a1a"><path d="M6.6 10.8a15 15 0 0 0 6.6 6.6l2.2-2.2c.3-.3.7-.4 1-.2 1.1.4 2.3.6 3.6.6.6 0 1 .4 1 1V20c0 .6-.4 1-1 1A17 17 0 0 1 3 4c0-.6.4-1 1-1h3.5c.6 0 1 .4 1 1 0 1.3.2 2.5.6 3.6.1.3 0 .7-.2 1z"/></svg>206-555-0147</div>

<h2 class="abs center sec-title" style="top:1002px">Our Services</h2>
<section class="abs services">
  <div class="service s1" role="img" aria-label="Transportation: white trailer truck on a road">
    <span class="ico"><svg width="24" height="24" viewBox="0 0 24 24" fill="#fff"><path d="M1 6h13v10H1zM15 9h4l3 4v3h-7z"/><circle cx="5" cy="18" r="2"/><circle cx="18" cy="18" r="2"/></svg></span>
    <h3>Transportation</h3>
  </div>
  <div class="service active">
    <span class="ico"><svg width="24" height="24" viewBox="0 0 24 24" fill="none" stroke="#fff" stroke-width="2"><path d="M3 11 12 4l9 7v9H3z M9 20v-5h6v5"/></svg></span>
    <h3>Warehousing</h3>
    <p>Lorem Ipsum is simply dummy text of the printing and typesetting industry. Lorem Ipsum has been the industry's standard...</p>
    <a class="btn">Our Services &#10140;</a>
  </div>
  <div class="service s3" role="img" aria-label="Consolidating: staff working on laptops in an office">
    <span class="ico"><svg width="24" height="24" viewBox="0 0 24 24" fill="#fff"><circle cx="8" cy="7" r="3"/><circle cx="16" cy="7" r="3"/><path d="M2 20c0-4 3-7 6-7s6 3 6 7zM12 20c0-4 2-7 4-7s6 3 6 7z"/></svg></span>
    <h3>Consolidating</h3>
  </div>
  <div class="service s4" role="img" aria-label="Loading: heavy truck at a loading area">
    <span class="ico"><svg width="24" height="24" viewBox="0 0 24 24" fill="#fff"><path d="M2 8h12v8H2zM15 10h4l3 3v3h-7z"/><circle cx="6" cy="18" r="2"/><circle cx="18" cy="18" r="2"/></svg></span>
    <h3>Loading</h3>
  </div>
</section>
<div class="abs pager" style="left:532px;top:1540px">
  <span class="prev"><svg width="20" height="10" viewBox="0 0 20 10"><path d="M20 5H2M6 1 2 5l4 4" stroke="#ec6a1a" stroke-width="1.5" fill="none"/></svg>PREV</span>
  <span class="next">NEXT<svg width="20" height="10" viewBox="0 0 20 10"><path d="M0 5h18M14 1l4 4-4 4" stroke="#222" stroke-width="1.5" fill="none"/></svg></span>
</div>

<section class="abs testimonials">
  <h2 class="abs center" style="top:62px;font-size:22px;color:#222;font-weight:500">What Our Customers Says</h2>
  <div class="abs arrow-btn" style="left:164px;top:207px"><svg width="14" height="10" viewBox="0 0 14 10"><path d="M14 5H2M5 1 1 5l4 4" stroke="#999" stroke-width="1.5" fill="none"/></svg></div>
  <div class="abs arrow-btn" style="left:1000px;top:207px;border-color:var(--orange)"><svg width="14" height="10" viewBox="0 0 14 10"><path d="M0 5h12M9 1l4 4-4 4" stroke="#ec6a1a" stroke-width="1.5" fill="none"/></svg></div>
  <div class="abs avatar" role="img" aria-label="Customer portrait"></div>
  <div class="abs qmark" style="left:380px;top:138px">&ldquo;</div>
  <p class="abs quote">Lorem Ipsum is simply dummy text of the printing and typesetting industry. Lorem Ipsum has been the industry's standard dummy text ever since the 1500s, when an unknown printer took a galley of type and scrambled it to make a type specimen book.</p>
  <div class="abs qmark" style="left:800px;top:208px">&rdquo;</div>
  <div class="abs author">Marissa T.</div>
  <div class="abs author-meta">Cascade Provisions &nbsp;/&nbsp; San Diego, CA</div>
  <div class="abs dots"><span></span><span></span><span class="on"></span><span></span><span></span><span></span><span></span></div>
</section>

<h2 class="abs sec-title blog-head">Our Blogs</h2>
<div class="abs pager blog-pager">
  <span class="prev"><svg width="20" height="10" viewBox="0 0 20 10"><path d="M20 5H2M6 1 2 5l4 4" stroke="#ec6a1a" stroke-width="1.5" fill="none"/></svg>PREV</span>
  <span class="next">NEXT<svg width="20" height="10" viewBox="0 0 20 10"><path d="M0 5h18M14 1l4 4-4 4" stroke="#222" stroke-width="1.5" fill="none"/></svg></span>
</div>
<div class="abs blog-rule"></div>
<article class="abs blog-feature" role="img" aria-label="Red semi truck with white trailer on a road at dusk">
  <h4>Lorem ipsum is simply dummy text</h4>
  <div class="date">29-Jan-2017</div>
  <p>It has survived not only five centuries, but also the leap into electronic typesetting, remaining...</p>
  <div class="more">Read More &#10140;</div>
</article>
<article class="abs blog-card" style="left:612px">
  <div class="top"><h4>Lorem Ipsum is simply dummy text</h4><div class="date">29-Jan-2017</div></div>
  <div class="body">It has survived not only five centuries, but also the leap into electronic typesetting, remaining...<div class="more">Read More &#10140;</div></div>
</article>
<article class="abs blog-card" style="left:840px">
  <div class="top"><h4>Lorem Ipsum is simply dummy text</h4><div class="date">17-Feb-2017</div></div>
  <div class="body">It has survived not only five centuries, but also the leap into electronic typesetting, remaining...<div class="more">Read More &#10140;</div></div>
</article>

<div class="abs map" role="img" aria-label="Street map around the company office"></div>

<footer class="abs footer">
  <div class="abs fcol" style="left:155px"><h5>Quick Links</h5>
    <ul><li class="on">Home</li><li>About Us</li><li>Services</li><li>Dispatch</li><li>Equipment</li><li>Safety</li><li>Insurance</li><li>Contact Us</li></ul></div>
  <div class="abs fcol" style="left:383px"><h5>Our Services</h5>
    <ul><li>Transportation</li><li>Consolidating</li><li class="on">Warehousing</li><li>Loading</li><li>Distribution Services</li></ul></div>
  <div class="abs fcol" style="left:612px"><h5>Our Support</h5>
    <ul><li>Employment</li><li>Insurance</li><li>Safety</li><li>Equipment</li><li>Dispatch</li><li>Privacy Policy</li></ul></div>
  <div class="abs fcol fcontact" style="left:840px"><h5>Contact Us</h5>
    <ul>
      <li><svg width="10" height="12" viewBox="0 0 24 24" fill="#ec6a1a"><path d="M12 22s7-7 7-12a7 7 0 0 0-14 0c0 5 7 12 7 12z"/></svg><span>27/412 Harlow Rd<br>Glenmere Park VIC 3150</span></li>
      <li><svg width="10" height="12" viewBox="0 0 24 24" fill="#ec6a1a"><path d="M6.6 10.8a15 15 0 0 0 6.6 6.6l2.2-2.2c.3-.3.7-.4 1-.2 1.1.4 2.3.6 3.6.6.6 0 1 .4 1 1V20c0 .6-.4 1-1 1A17 17 0 0 1 3 4c0-.6.4-1 1-1h3.5c.6 0 1 .4 1 1 0 1.3.2 2.5.6 3.6.1.3 0 .7-.2 1z"/></svg><span>Phone: + 206-555-0147</span></li>
      <li><svg width="11" height="12" viewBox="0 0 24 24" fill="none" stroke="#ec6a1a" stroke-width="2.5"><rect x="2" y="5" width="20" height="14"/><path d="m2 5 10 8 10-8"/></svg><span>Email:<br>orders@dastrelogourmet.example</span></li>
    </ul></div>
  <div class="abs totop"><svg width="12" height="8" viewBox="0 0 12 8"><path d="M1 7 6 2l5 5" stroke="#ec6a1a" stroke-width="1.8" fill="none"/></svg></div>
  <div class="abs copy">Copyright&copy; 2017 Dastrelo Trucking. All rights reserved.</div>
</footer>

</body>
</html>
```